Business Card Design using new logo

As much as we'd like to think that treating everyone equally is the best strategy for fairness, the reality is that the differences in the lives of women and men have to be taken into account to ensure that organizations, programs, services, and yes, even public policy treat women and men in ways that achieve gender equity.

That's where ParityLumen - fairness metrics insight comes in. Using the data-driven tools of gender analysis, our organization can help anyone determine if gender equity is being achieved - in businesses and organizations, in the planning and implementation of programs and services, and in the development and enforcement of public policy.
Updates

Apologies for the delay - have not had time to finalize the decision.  Should be early this week - probably Tuesday.

Industry/Entity Type

Business

Requirements
Must have
• New Logo for ParityLumen
• Logo plus words "Fairness Metrics Insight"

```html
<!DOCTYPE html>
<html lang="en">
<head>
<meta charset="utf-8">
<title>ParityLumen – Business Card</title>
<link rel="stylesheet" href="https://fonts.googleapis.com/css2?family=Ubuntu:wght@400;500&family=Arimo:wght@400&display=swap">
<style>
  :root {
    --backdrop: #c9cbcf;
    --backdrop-light: #dfe0e3;
    --card: #333333;
    --brand-grey: #c7c7c7;
    --text-grey: #bdbdbd;
    --accent: #f7941d;
    --divider: #6a6a6a;
  }
  * { margin: 0; padding: 0; box-sizing: border-box; }
  html, body {
    width: 1200px; height: 900px; overflow: hidden;
  }
  body {
    background: radial-gradient(ellipse at 50% 35%, var(--backdrop-light), var(--backdrop));
    font-family: "Arimo", Arial, sans-serif;
    position: relative;
  }
  .card {
    position: absolute;
    left: 300px;
    width: 600px;
    height: 343px;
    background: var(--card);
    border-radius: 26px;
    overflow: hidden;
    box-shadow: 0 6px 18px rgba(0,0,0,.18);
  }
  .card--front { top: 70px; }
  .card--back { top: 477px; }

  /* Front */
  .front-brand {
    position: absolute; top: 78px; left: 0; right: 0;
    text-align: center;
  }
  .brand-dot {
    display: inline-block; width: 54px; height: 54px;
    border-radius: 50%; background: var(--accent);
  }
  .front-brand .brand-name {
    display: block; margin-top: 10px;
    font-family: "Ubuntu", sans-serif; font-weight: 400;
    font-size: 58px; letter-spacing: -0.5px; line-height: 1;
    color: var(--brand-grey);
  }
  .front-brand .tagline {
    display: block; margin-top: 6px;
    font-family: "Arimo", sans-serif; font-size: 18px;
    color: var(--accent);
  }
  .front-bar {
    position: absolute; left: 60px; right: 0; top: 268px;
    height: 9px; background: var(--brand-grey);
  }

  /* Back */
  .back-brand {
    position: absolute; top: 40px; left: 40px;
    display: flex; align-items: center; gap: 14px;
  }
  .back-brand .brand-dot { width: 46px; height: 46px; }
  .back-brand .brand-name {
    font-family: "Ubuntu", sans-serif; font-size: 44px;
    color: var(--brand-grey); letter-spacing: -0.4px; line-height: 1;
  }
  .person {
    position: absolute; left: 40px; top: 120px;
    color: var(--text-grey); font-size: 14px; line-height: 1.25;
  }
  .person .name { color: var(--accent); font-size: 22px; line-height: 1.1; }
  .person .role { margin-bottom: 22px; }
  .label { color: var(--accent); }
  .office {
    position: absolute; left: 330px; top: 116px;
    padding-left: 14px; border-left: 1px solid var(--divider);
    color: var(--text-grey); font-size: 13.5px; line-height: 1.3;
  }
  .office .web { color: var(--accent); }
  .accent-arrow {
    position: absolute; left: 0; top: 236px;
  }
</style>
</head>
<body>
  <section class="card card--front" aria-label="Card front">
    <div class="front-brand">
      <span class="brand-dot"></span>
      <span class="brand-name">ParityLumen</span>
      <span class="tagline">Fairness Metrics Insight</span>
    </div>
    <div class="front-bar"></div>
  </section>

  <section class="card card--back" aria-label="Card back">
    <div class="back-brand">
      <span class="brand-dot"></span>
      <span class="brand-name">ParityLumen</span>
    </div>
    <div class="person">
      <div class="name">Marlo Kensington</div>
      <div class="role">General Manager</div>
      <div>Fairness Metrics Insight LLC</div>
      <div><span class="label">C:</span> + 00 12 345 6789</div>
      <div><span class="label">E:</span> Marlo@ParityLumen.com</div>
    </div>
    <div class="office">
      <div><span class="label">P:</span> + 00 12 345 6789</div>
      <div><span class="label">F:</span> + 00 12 345 6789</div>
      <div class="web">www.ParityLumen.com</div>
    </div>
    <svg class="accent-arrow" width="600" height="40" viewBox="0 0 600 40" aria-hidden="true">
      <rect x="0" y="14" width="548" height="12" fill="#f7941d"/>
      <polygon points="540,2 566,20 540,38" fill="#f7941d"/>
    </svg>
  </section>
</body>
</html>
```